Kestrel Unity Parade 2013

I am seeking to create a flyer promoting the event May Day in Sydney. The Event is a March and will be taking place on the 5th May Sunday. The Projection of the flyer should be fresh and modern but capable of encapsulating values of struggle, justice and solidarity. It is an event that started in the late 1800's in a struggle to obtain the 8 hour day.
This flyer should capture the old logo with a fresh modern interpretation.
Updates

HI All, 

Can we add the following details to design. Apologies it came late, it just got forwarded onto me. 

Twitter (logo) @KestrelUnity
Facebook (logo) Unity Kestrel 2013

Thanks

Reason: I want to allow designers the opportunity to make revisions on their existing designs.

Reason: Last minute changes are not coming through.

Target Market(s)

General Public, Union Members, Workers, advocates of social justice and democracy

Industry/Entity Type

Event

Requirements
Must have
• Event Details:
Kestrel Unity Parade
Sunday May 5th
Assembling: 11:30am
Marching: 12:00pm
Assembly Point: Brindle Street outside Tolvern Hall, Sydney
Kestrel Unity Logo (See Attachment) This logo should be manipulated to show a fresh and modern aspect to it, whilst retaing the same characteristics.

Nice to have
• Themes of the flyer should capture the following ideas:
International Workers Solidarity
Workers Rights
Fight for the 8 hour day
location being Sydney Australia
Images of
People Rallying, protesting, marching

```html
<!DOCTYPE html>
<html lang="en">
<head>
<meta charset="utf-8">
<title>Kestrel Unity Parade 2013</title>
<link rel="stylesheet" href="https://fonts.googleapis.com/css2?family=Bebas+Neue&family=Arimo&display=swap">
<style>
  :root {
    --page: #ffffff;
    --sand: #d8b48c;
    --clay: #d9906d;
    --red: #d1383a;
    --red-deep: #c8302f;
    --banner: #1f1c1c;
    --title-red: #d85a5c;
    --title-shadow: #8a2a2b;
    --ink: #1a1414;
    --fist: #3d2626;
    --social-ink: #2b2222;
    --social-mark: #5b8bd0;
  }
  * { margin: 0; padding: 0; box-sizing: border-box; }
  html, body {
    width: 936px;
    height: 1200px;
    overflow: hidden;
    background: var(--page);
  }
  .flyer {
    position: relative;
    width: 936px;
    height: 1200px;
    background: var(--page);
  }
  .poster {
    position: absolute;
    left: 19px;
    top: 16px;
    width: 898px;
    height: 1166px;
    overflow: hidden;
    background: linear-gradient(180deg, var(--sand) 0%, var(--clay) 38%, var(--red) 68%, var(--red-deep) 100%);
  }
  .fist-artwork {
    position: absolute;
    left: 246px;
    top: 78px;
    width: 460px;
    height: 700px;
    background: radial-gradient(ellipse 48% 50% at 50% 42%, rgba(61,38,38,0.85) 0%, rgba(61,38,38,0.55) 55%, rgba(61,38,38,0) 100%);
  }
  .committee-mark {
    position: absolute;
    left: 54px;
    top: 28px;
    width: 264px;
    height: 264px;
    border-radius: 50%;
    background: var(--red);
    display: flex;
    align-items: center;
    justify-content: center;
    text-align: center;
    font-family: 'Bebas Neue', sans-serif;
    font-size: 46px;
    line-height: 1;
    color: #ffffff;
  }
  .title-banner {
    position: absolute;
    left: 186px;
    top: 778px;
    width: 578px;
    height: 124px;
    background: var(--banner);
    transform: rotate(-3.2deg);
    text-align: center;
    font-family: 'Bebas Neue', sans-serif;
    color: var(--title-red);
    text-shadow: 2px 2px 0 var(--title-shadow);
  }
  .title-banner .event-name {
    display: block;
    font-size: 66px;
    line-height: 1;
    padding-top: 12px;
  }
  .title-banner .event-date {
    display: block;
    font-size: 38px;
    line-height: 0.9;
  }
  .event-details {
    position: absolute;
    left: 300px;
    width: 570px;
    top: 918px;
    text-align: center;
    font-family: 'Bebas Neue', sans-serif;
    color: var(--ink);
  }
  .detail-label { font-size: 31px; line-height: 0.95; }
  .detail-value { font-size: 21px; line-height: 0.95; }
  .detail-address { font-size: 22px; line-height: 1; }
  .social-links {
    position: absolute;
    left: 0;
    width: 898px;
    padding-left: 215px;
    top: 1088px;
    display: flex;
    justify-content: center;
    gap: 14px;
    font-family: 'Arimo', sans-serif;
    font-size: 15px;
    color: var(--social-ink);
  }
  .social-item { display: flex; align-items: center; gap: 8px; }
  .social-item::before {
    content: "";
    width: 19px;
    height: 19px;
    background: var(--social-mark);
  }
</style>
</head>
<body>
  <main class="flyer">
    <section class="poster">
      <div class="fist-artwork" role="img" aria-label="Painted raised clenched fist, dark brown brush illustration"></div>

      <div class="committee-mark">Kestrel<br>Unity</div>

      <h1 class="title-banner">
        <span class="event-name">Kestrel Unity Parade</span>
        <span class="event-date">Sunday May 5th</span>
      </h1>

      <div class="event-details">
        <p class="detail-label">Assembling</p>
        <p class="detail-value">11:30AM</p>
        <p class="detail-label">Marching</p>
        <p class="detail-value">12:00PM</p>
        <p class="detail-label">Assembly Point</p>
        <p class="detail-address">Brindle Street outside Tolvern Hall, Sydney</p>
      </div>

      <div class="social-links">
        <span class="social-item">@KestrelUnity</span>
        <span class="social-item">Unity Kestrel 2013</span>
      </div>
    </section>
  </main>
</body>
</html>
```